International Heavy Earthmoving Freight forwarder needs a flyer design

We need a flyer design to send out on Linkedin, Facebook, e-mail blasts, instagram etc.
We would like to announce that we have just secured a new contract offering exceptionally low shipping rates from East Coast and Gulf USA to Indonesia, Malaysia, Thailand amongst other South East Asian countries.
I would like to make it an announcement like "Hot off the press"
You can visit our instagram page for photos @bravolane
I would like the contact person on the flyer to be:
Owen Tarrel
owen.tarrel@bravolane.example
+1 555 014 2268
www.bravolane.example

Target Market(s)

Import and export used machinery equioment dealers. Mining companies, earthmoving contractors, freight forwarders

Font styles to use
Sans Serif

Requirements
Must have
• Logo, contact details, some photos from various Bravolane media outlets

```html
<!DOCTYPE html>
<html lang="en">
<head>
<meta charset="utf-8">
<title>Bravolane – Low Shipping Rates Flyer</title>
<link rel="stylesheet" href="https://fonts.googleapis.com/css2?family=Montserrat:wght@700;800&family=Bebas+Neue&family=Lato:wght@400;700&display=swap">
<style>
  :root {
    --red: #d40b0b;
    --red-deep: #7a0606;
    --red-dark: #4e0303;
    --ink: #2a2a2a;
    --ink-soft: #3b3b3b;
    --white: #ffffff;
    --black: #111111;
  }
  * { margin: 0; padding: 0; box-sizing: border-box; }
  html, body { width: 902px; height: 1200px; overflow: hidden; background: var(--white); }
  .flyer { position: relative; width: 902px; height: 1200px; overflow: hidden; font-family: "Lato", sans-serif; }
  .flyer__backdrop { position: absolute; inset: 0; }

  .brand { position: absolute; left: 140px; top: 92px; display: flex; align-items: center; gap: 14px; }
  .brand__dot { width: 44px; height: 44px; border-radius: 50%; background: var(--red); }
  .brand__name { font-family: "Montserrat", sans-serif; font-weight: 800; font-size: 28px; color: var(--ink); letter-spacing: 0.5px; text-transform: uppercase; }

  .hero-photo {
    position: absolute; left: 424px; top: 0; width: 478px; height: 417px;
    background: linear-gradient(160deg, #ffffff 0%, #eef1f5 40%, #c9d6ea 70%, #e9ecf0 100%);
    border-bottom-left-radius: 60px;
    box-shadow: -4px 6px 14px rgba(0,0,0,0.25);
  }

  .headline { position: absolute; left: 39px; line-height: 1; }
  .headline--offering { top: 210px; font-family: "Montserrat", sans-serif; font-weight: 800; font-size: 78px; color: var(--ink); letter-spacing: 1px; }
  .headline--exceptionally { top: 290px; font-family: "Bebas Neue", sans-serif; font-size: 82px; color: var(--red); letter-spacing: 0.5px; }

  .offer { position: absolute; left: 40px; top: 390px; color: var(--white); font-family: "Bebas Neue", sans-serif; text-transform: uppercase; }
  .offer__rates { font-size: 80px; line-height: 1; letter-spacing: 0.5px; }
  .offer__origin { font-size: 48px; line-height: 1; margin-top: 14px; }
  .offer__destinations { font-size: 38px; line-height: 44px; margin-top: 14px; width: 720px; }

  .gallery { position: absolute; left: 41px; top: 655px; width: 802px; display: flex; justify-content: space-between; }
  .gallery__photo {
    width: 178px; height: 178px; border-radius: 50%;
    border: 4px solid var(--red); box-shadow: 0 0 0 4px var(--white), 0 6px 12px rgba(0,0,0,0.3);
  }
  .gallery__photo--loading { background: linear-gradient(160deg, #cfd6dc 0%, #b56a3a 50%, #3a3f48 100%); }
  .gallery__photo--vessel { background: linear-gradient(180deg, #5e6772 0%, #8b939c 45%, #2a3a48 70%, #4f8e94 100%); }
  .gallery__photo--truck { background: linear-gradient(180deg, #a9d1f0 0%, #4d8a4a 45%, #e6c229 65%, #6c6c6c 100%); }
  .gallery__photo--barge { background: linear-gradient(180deg, #8fc3e8 0%, #b8863e 50%, #2f7896 80%, #1f5f7a 100%); }

  .contact { position: absolute; left: 0; top: 871px; width: 902px; text-align: center; color: var(--ink-soft); }
  .contact__label {
    display: inline-block; height: 48px; line-height: 42px; padding: 0 24px; border: 2px solid var(--red); border-radius: 26px;
    font-weight: 700; font-size: 30px; color: var(--red); background: var(--white); letter-spacing: 0.5px;
  }
  .contact__name { font-weight: 700; font-size: 23px; line-height: 30px; margin-top: 22px; letter-spacing: 0.5px; }
  .contact__list { list-style: none; margin-top: 10px; }
  .contact__item { display: flex; justify-content: center; align-items: center; gap: 10px; font-size: 22px; font-weight: 700; height: 40px; }
  .contact__icon { width: 17px; height: 17px; fill: var(--red); }
</style>
</head>
<body>
<main class="flyer">
  <svg class="flyer__backdrop" width="902" height="1200" viewBox="0 0 902 1200" aria-hidden="true">
    <defs>
      <linearGradient id="headerFill" x1="0" y1="0" x2="0" y2="1">
        <stop offset="0" stop-color="#e4e4e4"/>
        <stop offset="0.5" stop-color="#ffffff"/>
      </linearGradient>
      <linearGradient id="bodyFill" x1="0" y1="0" x2="0" y2="1">
        <stop offset="0" stop-color="#ffffff"/>
        <stop offset="1" stop-color="#d9d9d9"/>
      </linearGradient>
      <radialGradient id="bandFill" cx="0.55" cy="0.45" r="0.7">
        <stop offset="0" stop-color="#8e0b0b"/>
        <stop offset="1" stop-color="#4e0303"/>
      </radialGradient>
    </defs>
    <rect width="902" height="370" fill="url(#headerFill)"/>
    <rect y="368" width="902" height="832" fill="url(#bodyFill)"/>
    <path d="M0 368 H902 V610 C720 625 420 620 0 640 Z" fill="url(#bandFill)"/>
    <path d="M0 640 C420 620 720 625 902 610 V640 C720 650 420 660 0 700 Z" fill="#d40b0b"/>
    <path d="M0 1000 Q451 1250 902 1000 V1200 H0 Z" fill="#111111"/>
    <path d="M0 1040 Q451 1252 902 1046 V1200 H0 Z" fill="#ffffff"/>
    <path d="M0 1052 Q451 1262 902 1058 V1200 H0 Z" fill="#d40b0b"/>
  </svg>

  <div class="brand">
    <span class="brand__dot"></span>
    <span class="brand__name">Bravolane</span>
  </div>

  <div class="hero-photo" role="img" aria-label="Air, sea, road and rail transport: cargo plane, ship, blue truck and high-speed train"></div>

  <h1 class="headline headline--offering">OFFERING</h1>
  <p class="headline headline--exceptionally">EXCEPTIONALLY</p>

  <section class="offer">
    <p class="offer__rates">Low Shipping Rates</p>
    <p class="offer__origin">From East Coast and Gulf USA</p>
    <p class="offer__destinations">To Indonesia, Malaysia, Thailand amongst other South East Asian countries</p>
  </section>

  <section class="gallery">
    <div class="gallery__photo gallery__photo--loading" role="img" aria-label="Worker loading machinery into a container"></div>
    <div class="gallery__photo gallery__photo--vessel" role="img" aria-label="Cargo vessel at sea under cloudy sky"></div>
    <div class="gallery__photo gallery__photo--truck" role="img" aria-label="Yellow truck hauling an oversized load"></div>
    <div class="gallery__photo gallery__photo--barge" role="img" aria-label="Crane loading heavy equipment onto a barge"></div>
  </section>

  <section class="contact">
    <h2 class="contact__label">CONTACT US</h2>
    <p class="contact__name">OWEN TARREL</p>
    <ul class="contact__list">
      <li class="contact__item">
        <svg class="contact__icon" viewBox="0 0 20 20"><path d="M1 4h18v12H1z M1 4l9 7 9-7" fill="#d40b0b" stroke="#fff" stroke-width="1.2"/></svg>
        owen.tarrel@bravolane.example
      </li>
      <li class="contact__item">
        <svg class="contact__icon" viewBox="0 0 20 20"><circle cx="10" cy="10" r="9" fill="none" stroke="#d40b0b" stroke-width="1.8"/><path d="M6.5 5.5l2 .2.8 2.3-1.2 1a6 6 0 0 0 3 3l1-1.2 2.3.8.2 2c-4.5.6-8.7-3.6-8.1-8.1z"/></svg>
        +1 555 014 2268
      </li>
      <li class="contact__item">
        <svg class="contact__icon" viewBox="0 0 20 20"><g fill="none" stroke="#d40b0b" stroke-width="1.6"><circle cx="10" cy="10" r="8"/><ellipse cx="10" cy="10" rx="3.5" ry="8"/><path d="M2 10h16"/></g></svg>
        www.bravolane.example
      </li>
    </ul>
  </section>
</main>
</body>
</html>
```